Cedar Hollow Growth Institute is changing lives and needs a state of the art PageLoom Business Web

We are looking for lots of WOW factor. We need a state of the art website that inspires people to take action toward changing their life. We have some award winning trademarked programs that we are looking to introduce through our website.

The Top Portion will have a place holder for a welcome video (currently being recorded) and this brief description of the business along side of it:
=====================================================
Let’s face it. Life is hard. Being human isn’t easy for any of us. Here, at the Cedar Hollow Growth Institute, we understand that simple truth. We know that having a strong self-worth first requires you to be aware of your value as a Human Being. Human potential is the HIGHEST value that creation has to offer.

Regardless of whether you see it through the eyes of evolution or through the eyes of religion, the truth of the matter is that Human Beings are of significant value. Abundance is our birthright! Our focus is on developing that human potential.

There is only one thing holding you back from experiencing overflowing abundance – YOU! Ask yourself, why haven’t I experienced that true transformation, in my life, that attracts abundance?

What if there was a way to remove the uncertainty tied to the labyrinth of life? What if you no longer have to be a victim of the unpredictable? Well, the good news is – Its Possible! There is an amazing amount of potential locked away deep inside you. Potential that has the capacity to release you from your current patterns of thinking and launch a complete turning point in your life.

The Cedar Hollow Growth Institute recognizes this potential, often before you recognize it in yourself, and is excited to partner with you on your journey to becoming an unstoppable force. We look forward to resourcing you with the tools and training that will help you synchronize your desire and your direction with your destiny!
============================================================

Under the welcome / intro block, we would like to have a gallery that scrolls through pictures, and inspirational quotes. We can also use this to advertise
our services and special deals on programs.

Next section can outline our lanes of business or focus areas:

High Performance Living
Business Coaching & Consultancy
Digital Resources Center

Here is the template we would like to leverage: https://pageloom-sites.example/theme/harvestline
or you can be creative and provide one you think would work best....

Should have some awesome photos, descriptions, etc....

Here are some samples to model after:

https://vantorix.example/
https://www.kelvo-mentoring.example/
http://dorianwexley.example/

https://brennocorteam.example/talk/?c=brc-se-bo&brtc=brt-core&gclid=QzLmPfRtYvWxNcBaKjHgDsEuIoPaLkMnBvCxZqWeRtYuIoPaSdFgHjKlZxCvBnMqWeRtYuIoPaSdFg

https://laurent-okafor.example/
https://www.mymindforge.example/
https://www.tobiasfenwick.example/

Target Market(s)

Business Leaderships and anyone interested in personal development and growth

Industry/Entity Type

Leadership

Coding

Coded - Design and coding required

Font styles to use
Serif
Sans Serif
Decorative
Script

Colors

Designer to choose colors to be used in the design.

Requirements
Must have
• Business Name, Logo, and brief introduction paragraph. Must have space for the welcome video.
• We do not have any current site but do already own the domain for it:
• https://chgrow.example/ is the PageLoom site we will be using once we choice a winner to work with
• Must use our Taglines:
• Shaping the existence of individuals, organizations, and communities...
• Make your life the grandest parade in town!
• =====================================================
• Would like music to softly play in back ground when people land on the page. This song could repeat in the background: https://www.vidstreamo.example/watch?v=QxTr7vLmNaP&list=ZKw3HtYbRcUoFgEiMnJsLpQaVdXzCyBt92&index=4
• You can also cycle through the entire soundtrack of the RINGMASTER'S DREAM - all those songs work perfectly with our themes
• You must also blend the content available on this site with the new site:
• https://www.brennocorgroup.example/dwaynehollister
Nice to have
• would like music to softly play in back ground when people land on the page. This song could repeat in the softly in the background: https://www.vidstreamo.example/watch?v=QxTr7vLmNaP&list=ZKw3HtYbRcUoFgEiMnJsLpQaVdXzCyBt92&index=4
Should not have
• Ads, empty white space, negative perspectives, etc....

```html
<!DOCTYPE html>
<html lang="en">
<head>
<meta charset="utf-8">
<title>Cedar Hollow Growth Institute</title>
<link href="https://fonts.googleapis.com/css2?family=Marcellus&family=Roboto:ital,wght@0,400;0,500;0,700;1,400;1,700&display=swap" rel="stylesheet">
<style>
:root{
  --ink:#000000;
  --white:#ffffff;
  --navy:#262a73;
  --navy-deep:#1b1f5e;
  --slate:#4a4a4d;
  --slate-dark:#3c3c3f;
  --card-label:#4d4d50;
}
*{margin:0;padding:0;box-sizing:border-box}
html,body{width:1200px;height:2778px;overflow:hidden;background:var(--ink)}
body{position:relative;font-family:"Roboto",Arial,sans-serif;color:var(--white);-webkit-font-smoothing:antialiased}

/* Header */
.site-header{position:absolute;top:0;left:0;width:1200px;height:130px;z-index:5}
.brand{position:absolute;left:172px;top:34px;width:190px;text-align:center;display:flex;flex-direction:column;align-items:center}
.brand-mark{width:40px;height:40px;border-radius:50%;border:2px solid var(--white);margin-bottom:8px}
.brand-name{font-family:"Marcellus",Georgia,serif;font-size:19px;line-height:22px;color:var(--white)}
.main-nav{position:absolute;top:60px;left:462px;display:flex;align-items:center}
.main-nav a{color:var(--white);text-decoration:none;font-size:15px;font-weight:500;margin-right:44px;letter-spacing:.2px}
.search-icon{width:16px;height:16px}

/* Hero */
.hero{position:absolute;top:0;left:0;width:1200px;height:656px;
  background:linear-gradient(180deg,#2b3a83 0%,#2f6b9c 38%,#5fc6cf 62%,#9fe9e4 72%,#1a2a3a 88%,#050808 100%)}
.hero-photo{position:absolute;inset:0;background:radial-gradient(ellipse at 75% 55%,rgba(160,240,235,.55),rgba(0,0,0,0) 55%),linear-gradient(180deg,rgba(0,0,0,0) 55%,rgba(0,0,0,.85) 100%)}
.hero-copy{position:absolute;left:658px;top:194px;width:530px}
.hero-title{font-family:"Marcellus",Georgia,serif;font-weight:400;font-size:29.5px;line-height:39px;letter-spacing:.6px;text-transform:uppercase;color:var(--white)}
.hero-tagline{font-family:"Marcellus",Georgia,serif;font-size:22px;margin-top:12px;color:var(--white)}
.btn-services{position:absolute;left:659px;top:383px;width:162px;height:48px;border-radius:24px;background:var(--navy-deep);color:var(--white);font-size:12px;font-weight:700;display:flex;align-items:center;justify-content:center;gap:8px;letter-spacing:.4px}
.play-button{position:absolute;left:1051px;top:508px;width:84px;height:84px}
.section-ghost{position:absolute;font-family:"Marcellus",Georgia,serif;font-size:90px;letter-spacing:4px;color:rgba(255,255,255,.07)}

/* About */
.about{position:absolute;top:656px;left:0;width:1200px;height:540px;background:var(--ink)}
.about-body{position:absolute;top:72px;left:190px;width:820px;text-align:center;color:var(--white)}
.about-body p{color:var(--white);font-weight:400}
.about-lead{font-size:15.5px;line-height:28px;padding:0 18px}
.about-small{font-size:12.5px;line-height:28px}
.divider-mark{position:absolute;left:576px;width:48px;height:48px;border-radius:50%;border:3px solid var(--white);background:var(--slate-dark);z-index:3}

/* Gallery */
.gallery{position:absolute;top:1196px;left:0;width:1200px;height:684px;background:linear-gradient(180deg,var(--slate) 0%,#555558 60%,var(--slate-dark) 100%)}
.section-title{position:absolute;left:0;width:1200px;text-align:center;font-family:"Marcellus",Georgia,serif;font-weight:400;font-size:37px;letter-spacing:1px;display:flex;align-items:center;justify-content:center;gap:20px;color:var(--white)}
.section-title::before,.section-title::after{content:"";width:64px;height:4px;background:var(--white)}
.slide{position:absolute;overflow:hidden}
.slide-quote{position:absolute;left:26px;bottom:30px;width:300px;font-size:12px;font-weight:700;font-style:italic;line-height:22px;color:var(--white)}
.slide-center .slide-quote{left:70px;width:300px;text-align:center}
.slider-nav{position:absolute;top:1752px;left:522px;display:flex;align-items:center;gap:10px}
.nav-circle{width:32px;height:32px;border-radius:50%;border:2px solid var(--white);display:flex;align-items:center;justify-content:center}

/* Focus */
.focus{position:absolute;top:1880px;left:0;width:1200px;height:584px;background:linear-gradient(180deg,var(--navy) 0%,#2a2f7c 55%,var(--navy-deep) 100%)}
.focus-card{position:absolute;width:261px}
.focus-image{height:180px}
.focus-label{position:relative;height:57px;background:var(--card-label);text-align:center;font-size:14px;font-weight:700;padding-top:26px;color:var(--white)}
.focus-icon{position:absolute;left:112px;top:-20px;width:38px;height:38px;border-radius:50%;background:var(--card-label);display:flex;align-items:center;justify-content:center}

/* Footer */
.site-footer{position:absolute;top:2464px;left:0;width:1200px;height:314px;background:var(--ink)}
.social-row{position:absolute;top:71px;left:422px;display:flex;gap:11px}
.social-link{width:52px;height:52px;border-radius:50%;border:1.5px solid var(--white);display:flex;align-items:center;justify-content:center}
.social-dot{width:10px;height:10px;border-radius:50%;background:var(--white)}
.footer-nav{position:absolute;top:157px;left:0;width:1200px;text-align:center;font-size:14px;font-weight:500}
.footer-nav a{color:var(--white);text-decoration:none}
.footer-nav i{font-style:normal;margin:0 11px}
.footer-contact{position:absolute;top:200px;left:0;width:1200px;text-align:center;font-size:11.5px;display:flex;justify-content:center;align-items:center;gap:8px;color:var(--white)}
.footer-contact svg{width:11px;height:11px}
.copyright{position:absolute;top:236px;left:0;width:1200px;text-align:center;font-size:11.5px;color:var(--white)}
</style>
</head>
<body>

<header class="site-header">
  <div class="brand">
    <span class="brand-mark"></span>
    <span class="brand-name">Cedar Hollow<br>Growth Institute</span>
  </div>
  <nav class="main-nav">
    <a href="#">HOME</a><a href="#">ABOUT US</a><a href="#">SERVICES</a><a href="#">FOCUS AREA</a><a href="#">CONTACT US</a>
    <svg class="search-icon" viewBox="0 0 16 16"><circle cx="6.5" cy="6.5" r="4.8" fill="none" stroke="#fff" stroke-width="2.2"/><line x1="10" y1="10" x2="14.5" y2="14.5" stroke="#fff" stroke-width="2.6" stroke-linecap="round"/></svg>
  </nav>
</header>

<section class="hero">
  <div class="hero-photo" role="img" aria-label="Silhouettes of people helping each other climb a rocky summit against a bright teal sky"></div>
  <div class="hero-copy">
    <h1 class="hero-title">Shaping the existence<br>of individuals,organizations<br>&amp; communities...</h1>
    <p class="hero-tagline">Make your life the grandest parade in town!</p>
  </div>
  <a class="btn-services">VIEW SERVICES
    <svg width="13" height="13" viewBox="0 0 14 14"><circle cx="7" cy="7" r="7" fill="#fff"/><path d="M5.5 4 L9 7 L5.5 10" fill="none" stroke="#1b1f5e" stroke-width="2"/></svg>
  </a>
  <svg class="play-button" viewBox="0 0 84 84" aria-label="Play welcome video"><circle cx="42" cy="42" r="38" fill="rgba(255,255,255,.1)" stroke="#fff" stroke-width="5"/><path d="M33 27 L59 42 L33 57 Z" fill="#fff"/></svg>
  <div class="section-ghost" style="left:18px;top:560px">ABOUT</div>
</section>

<section class="about">
  <div class="about-body">
    <p class="about-lead">Let’s face it. Life is hard. Being human isn’t easy for any of us. Here, at the Cedar Hollow Growth Institute, we understand that simple truth. We know that having a strong self-worth first requires you to be aware of your value as a Human Being. Human potential is the HIGHEST value that creation has to offer.</p>
    <p class="about-small">Regardless of whether you see it through the eyes of evolution or through the eyes of religion, the truth of the matter is that Human Beings are of significant value. Abundance is our birthright! Our focus is on developing that human potential.</p>
    <p class="about-small">There is only one thing holding you back from experiencing overflowing abundance – YOU! Ask yourself, why haven’t I experienced that true transformation, in my life, that attracts abundance? What if there was a way to remove the uncertainty tied to the labyrinth of life? What if you no longer have to be a victim of the unpredictable? Well, the good news is – Its Possible!</p>
    <p class="about-small">There is an amazing amount of potential locked away deep inside you. Potential that has the capacity to release you from your current patterns of thinking and launch a complete turning point in your life.</p>
    <p class="about-lead">The Cedar Hollow Growth Institute recognizes this potential, often before you recognize it in yourself, and is excited to partner with you on your journey to becoming an unstoppable force. We look forward to resourcing you with the tools and training that will help you synchronize your desire and your direction with your destiny!</p>
  </div>
</section>
<span class="divider-mark" style="top:1172px"></span>

<section class="gallery">
  <div class="section-ghost" style="left:10px;top:40px">GALLERY</div>
</section>
<h2 class="section-title" style="top:1290px">GALLERY</h2>
<div class="slide" style="left:0;top:1369px;width:381px;height:331px;background:linear-gradient(180deg,#4a5b7a 0%,#c98a4a 55%,#2a1a10 100%)" role="img" aria-label="Silhouettes of climbers reaching for each other at sunset">
  <p class="slide-quote">“ At vero eos et accusamus et iusto odio dignissimos ducimus qui blanditiis praesentium voluptatum ”</p>
</div>
<div class="slide slide-center" style="left:381px;top:1391px;width:438px;height:331px;background:linear-gradient(180deg,#9fb3c2 0%,#c9c8b8 55%,#6b6a5e 100%)" role="img" aria-label="Woman seen from behind raising both arms toward an open sky">
  <p class="slide-quote">“ At vero eos et accusamus et iusto odio dignissimos ducimus qui blanditiis praesentium voluptatum ”</p>
</div>
<div class="slide" style="left:819px;top:1369px;width:381px;height:331px;background:linear-gradient(180deg,#8fb4d8 0%,#4f6f98 55%,#1e3050 100%)" role="img" aria-label="Hiker standing on a mountain peak above blue ridges">
  <p class="slide-quote">“ At vero eos et accusamus et iusto odio dignissimos ducimus qui blanditiis praesentium voluptatum ”</p>
</div>
<div class="slider-nav">
  <svg width="28" height="12" viewBox="0 0 28 12"><path d="M27 6 H2 M7 1 L2 6 L7 11" fill="none" stroke="#fff" stroke-width="2"/></svg>
  <span class="nav-circle"><svg width="10" height="12" viewBox="0 0 10 12"><path d="M7 1 L2 6 L7 11" fill="none" stroke="#fff" stroke-width="2"/></svg></span>
  <span class="nav-circle"><svg width="10" height="12" viewBox="0 0 10 12"><path d="M3 1 L8 6 L3 11" fill="none" stroke="#fff" stroke-width="2"/></svg></span>
  <svg width="28" height="12" viewBox="0 0 28 12"><path d="M1 6 H26 M21 1 L26 6 L21 11" fill="none" stroke="#fff" stroke-width="2"/></svg>
</div>
<span class="divider-mark" style="top:1856px"></span>

<section class="focus">
  <div class="section-ghost" style="left:890px;top:80px">FOCUS</div>
</section>
<h2 class="section-title" style="top:1985px">FOCUS AREA</h2>
<div class="focus-card" style="left:176px;top:2083px">
  <div class="focus-image" role="img" aria-label="Hand touching glowing hexagon icons of success and excellence" style="background:linear-gradient(135deg,#bfe6f0 0%,#5aa2c4 50%,#1d3f62 100%)"></div>
  <div class="focus-label"><span class="focus-icon"><svg width="20" height="20" viewBox="0 0 20 20"><circle cx="10" cy="6" r="4" fill="#fff"/><path d="M2 19 C2 12 18 12 18 19 Z" fill="#fff"/></svg></span>High Performance Living</div>
</div>
<div class="focus-card" style="left:470px;top:2098px">
  <div class="focus-image" role="img" aria-label="Hand drawing a glowing figure climbing rising steps" style="background:linear-gradient(135deg,#0f2538 0%,#2f6f93 55%,#b8c9d0 100%)"></div>
  <div class="focus-label"><span class="focus-icon"><svg width="22" height="20" viewBox="0 0 22 20"><circle cx="11" cy="5" r="3.4" fill="#fff"/><circle cx="4.5" cy="8" r="2.5" fill="#fff"/><circle cx="17.5" cy="8" r="2.5" fill="#fff"/><path d="M5 18 C5 10 17 10 17 18 Z M0 18 C0 12 6 12 6 15 V18 Z M22 18 C22 12 16 12 16 15 V18 Z" fill="#fff"/></svg></span>Business Coaching &amp; Consultancy</div>
</div>
<div class="focus-card" style="left:765px;top:2083px">
  <div class="focus-image" role="img" aria-label="Hand pointing a pen at financial charts on a glowing screen" style="background:linear-gradient(135deg,#16314a 0%,#2c6b8a 50%,#c9a07a 100%)"></div>
  <div class="focus-label"><span class="focus-icon"><svg width="20" height="18" viewBox="0 0 20 18"><rect x="1" y="1" width="18" height="12" rx="1" fill="none" stroke="#fff" stroke-width="2"/><rect x="8" y="13" width="4" height="3" fill="#fff"/><rect x="5" y="16" width="10" height="2" fill="#fff"/></svg></span>Digital Resources Center</div>
</div>
<span class="divider-mark" style="top:2440px"></span>

<footer class="site-footer">
  <div class="social-row" aria-label="Social profiles">
    <a class="social-link" href="#" aria-label="Social profile"><span class="social-dot"></span></a>
    <a class="social-link" href="#" aria-label="Social profile"><span class="social-dot"></span></a>
    <a class="social-link" href="#" aria-label="Social profile"><span class="social-dot"></span></a>
    <a class="social-link" href="#" aria-label="Video channel"><span class="social-dot"></span></a>
    <a class="social-link" href="#" aria-label="Social profile"><span class="social-dot"></span></a>
    <a class="social-link" href="#" aria-label="Email"><svg width="16" height="12" viewBox="0 0 16 12"><rect x="0" y="0" width="16" height="12" rx="1" fill="#fff"/><path d="M0 1 L8 7 L16 1" fill="none" stroke="#000" stroke-width="1.4"/></svg></a>
  </div>
  <nav class="footer-nav">
    <a href="#">HOME</a><i>/</i><a href="#">ABOUT US</a><i>/</i><a href="#">SERVICES</a><i>/</i><a href="#">FOCUS AREA</a><i>/</i><a href="#">CONTACT US</a>
  </nav>
  <div class="footer-contact">
    <svg viewBox="0 0 12 12"><path d="M6 0 C2.5 0 1.5 3 2 5 L6 12 L10 5 C10.5 3 9.5 0 6 0 Z" fill="#fff"/><circle cx="6" cy="4.2" r="1.6" fill="#000"/></svg>
    <span>233,Sed ut perspiciatis unde omnis iste</span><span>|</span>
    <svg viewBox="0 0 12 12"><path d="M2 0 L4.5 0 L5.5 3 L4 4.3 C4.8 6 6 7.2 7.7 8 L9 6.5 L12 7.5 V10 C12 11 11 12 10 12 C4.5 12 0 7.5 0 2 C0 1 1 0 2 0 Z" fill="#fff"/></svg>
    <span>Phone : 1 555 014 2270</span><span>|</span>
    <svg viewBox="0 0 12 12"><rect x="0" y="2" width="12" height="8" fill="#fff"/><path d="M0 2 L6 7 L12 2" fill="none" stroke="#000" stroke-width="1.2"/></svg>
    <span>hello@cedarhollow.example</span>
  </div>
  <p class="copyright">© 2019 Cedar Hollow.All Rights Reserved &nbsp;|&nbsp; Privacy Policy</p>
</footer>

</body>
</html>
```